Flooring Company Wordpress Design Using Elementor

We need a website design using elementor for a flooring company. I have attached a word document with the entire content for the site. I have sample websites www.pellmarbuildersnevada.com and www.tilbrookfinishesreno.com

The site needs to look alot better than the samples. Modern and professional is what we are looking for. 100 times better than the sample websites.

I have images to be used in the site but the file is to large to attached here.

```html
<!DOCTYPE html>
<html lang="en">
<head>
<meta charset="utf-8">
<title>Keystone Flooring Florida</title>
<link rel="stylesheet" href="https://fonts.googleapis.com/css2?family=Montserrat:wght@500;600;700&family=Lato:ital,wght@0,400;0,700;1,400&display=swap">
<style>
:root{
  --brown:#6e4220;
  --brown-mid:#8a5a2e;
  --accent:#a86e36;
  --ink:#1b1b1b;
  --text:#666;
  --line:#e6e6e6;
  --soft:#f3f3f3;
  --footer:#333;
  --white:#fff;
}
*{box-sizing:border-box;margin:0;padding:0}
html,body{width:1200px;height:4906px;overflow:hidden}
body{font-family:"Lato",sans-serif;color:var(--text);background:var(--white);position:relative}
h1,h2,h3,h4,.nav,.btn,.link{font-family:"Montserrat",sans-serif}
.link{font-size:12px;font-weight:600;color:var(--brown);text-decoration:underline;letter-spacing:.3px}
.link::after{content:" »"}
.btn{display:inline-flex;align-items:center;gap:10px;font-size:13px;font-weight:600;color:var(--white);background:var(--brown);padding:0 18px;height:42px;border-radius:3px;text-transform:uppercase}
.btn.accent{background:var(--accent)}
.btn i{width:13px;height:13px;border-radius:50%;background:var(--white);display:inline-block;position:relative}
.btn i::after{content:"";position:absolute;left:4px;top:3.5px;border-left:5px solid var(--brown);border-top:3px solid transparent;border-bottom:3px solid transparent}
.btn.accent i::after{border-left-color:var(--accent)}
.photo{display:block}

/* header */
.site-header{position:absolute;top:0;left:0;width:1200px;height:88px;display:flex;align-items:center;padding:0 90px}
.brand{display:flex;align-items:center;gap:14px}
.brand-mark{width:44px;height:44px;background:var(--accent)}
.brand-name{font-family:"Montserrat",sans-serif;font-weight:700;color:var(--brown);font-size:26px;line-height:1}
.brand-name small{display:block;font-size:12px;letter-spacing:.5px;margin-top:4px}
.nav{display:flex;gap:14px;margin-left:70px;font-size:13px;font-weight:600;color:var(--ink)}
.nav .active{color:var(--accent)}
.site-header .btn{margin-left:auto}

.hero{position:absolute;top:88px;left:0;width:1200px;height:560px;background:linear-gradient(180deg,#eef0ef 0%,#dcdcd6 45%,#a66d3e 75%,#7c4a25 100%)}

/* intro */
.intro{position:absolute;top:648px;left:0;width:1200px;height:512px;text-align:center;border-bottom:1px solid var(--line)}
.intro h1{margin:76px auto 0;width:760px;font-size:33px;line-height:52px;font-weight:700;color:var(--ink);text-transform:uppercase}
.intro p{margin-top:34px;font-size:15px;line-height:36px}
.intro .actions{margin-top:32px;display:flex;justify-content:center;gap:18px}

/* features */
.features{position:absolute;top:1160px;left:0;width:1200px;height:460px;display:flex;justify-content:center;gap:50px;padding-top:62px}
.feature{width:282px;text-align:center}
.icon-ring{width:86px;height:86px;border-radius:50%;border:3px solid var(--accent);margin:0 auto;display:flex;align-items:center;justify-content:center}
.feature h3{margin-top:40px;font-size:18px;line-height:26px;font-weight:700;color:var(--ink)}
.feature p{margin-top:22px;font-size:13.5px;line-height:24px}
.feature .link{display:inline-block;margin-top:14px}

/* partner */
.partner{position:absolute;top:1620px;left:0;width:1200px;height:488px;background:var(--soft)}
.partner .photo{position:absolute;right:0;top:0;width:620px;height:488px;background:linear-gradient(90deg,#f3f3f3 0%,#c9a985 30%,#9b6c44 70%,#6b4425 100%)}
.partner .copy{position:absolute;left:110px;top:52px;width:480px}
.partner h2{font-size:28px;line-height:36px;font-weight:700;color:var(--ink)}
.partner p{margin-top:26px;font-size:13.5px;line-height:30px}
.partner .btn{margin-top:26px}

/* services */
.services{position:absolute;top:2108px;left:0;width:1200px;height:1212px}
.section-title{font-size:29px;line-height:43px;font-weight:700;color:var(--ink);text-align:center;text-transform:uppercase}
.services .section-title{margin-top:70px}
.service-grid{position:absolute;top:212px;left:103px;display:grid;grid-template-columns:repeat(3,315px);gap:26px 25px}
.service-card{height:437px;background:var(--white);box-shadow:0 0 6px rgba(0,0,0,.16);text-align:center;padding:4px}
.service-card h3{font-size:16px;font-weight:600;color:var(--ink);line-height:56px}
.service-card .photo{height:204px;margin:0 0}
.service-card p{margin:36px 22px 0;font-size:13.5px;line-height:26px}
.service-card .link{display:inline-block;margin-top:8px}

/* testimonials */
.testimonials{position:absolute;top:3320px;left:0;width:1200px;height:370px;background:linear-gradient(180deg,#a47446,#9c6a3b 50%,#a8794c)}
.testimonials h2{position:absolute;left:382px;top:84px;font-size:29px;font-weight:700;color:var(--white)}
.slider-arrows{position:absolute;right:112px;top:42px;display:flex;gap:10px}
.slider-arrows span{width:34px;height:34px;background:var(--white);display:flex;align-items:center;justify-content:center}
.avatar{position:absolute;left:166px;top:150px;width:114px;height:114px;border-radius:50%;background:#d9d0c6}
.divider{position:absolute;left:326px;top:150px;width:2px;height:116px;background:rgba(255,255,255,.55)}
.quote-mark{position:absolute;left:364px;top:152px}
.testimonials blockquote{position:absolute;left:424px;top:152px;width:650px;font-style:italic;font-size:13.5px;line-height:26px;color:var(--white)}
.testimonials .btn{position:absolute;left:424px;top:250px}
.testimonials cite{position:absolute;left:906px;top:256px;font-style:normal;font-family:"Montserrat",sans-serif;font-size:18px;font-weight:500;color:var(--white)}

/* process */
.process{position:absolute;top:3690px;left:0;width:1200px;height:578px;text-align:center}
.process .section-title{margin-top:80px}
.steps{display:flex;justify-content:center;gap:0;margin-top:50px}
.step{width:250px}
.step svg{display:block;margin:0 auto}
.step h4{margin-top:26px;font-size:14px;line-height:22px;font-weight:700;color:var(--ink)}
.step p{margin:26px 20px 0;font-size:13.5px;line-height:24px}
.step .link{display:inline-block;margin-top:18px}

/* get started */
.get-started{position:absolute;top:4190px;left:0;width:1200px;height:350px;background:linear-gradient(180deg,rgba(255,255,255,0) 0%,#f4f0ec 40%,#ece4dc 100%)}
.get-started .section-title{margin-top:36px}
.form-row{position:absolute;left:110px;display:flex;align-items:center}
.form-row label{width:260px;font-family:"Montserrat",sans-serif;font-size:20px;font-weight:700;color:var(--ink)}
.form-row .field{width:236px;height:50px;margin-right:4px;background:var(--white);border:1px solid var(--line);font-size:13.5px;color:#888;padding:0 14px;display:flex;align-items:center}
.row-one{top:146px}
.row-two{top:214px}

/* footer */
.site-footer{position:absolute;top:4540px;left:0;width:1200px;height:328px;background:var(--footer);color:var(--white);font-size:13.5px}
.site-footer .brand{position:absolute;left:122px;top:60px}
.site-footer .brand-mark{background:var(--white);width:46px;height:46px}
.site-footer .brand-name{color:var(--white)}
.footer-about{position:absolute;left:122px;top:156px;width:240px;line-height:22px}
.footer-col{position:absolute;top:50px}
.footer-col h4{font-size:13px;font-weight:600;text-decoration:underline;margin-bottom:18px}
.footer-col li{list-style:none;line-height:38.5px;display:flex;align-items:center;gap:18px}
.footer-col li::before{content:"»";color:var(--accent)}
.contact li{gap:18px}
.contact li::before{content:none}
.contact .ic{width:14px;color:var(--accent);text-align:center}
.col-contact{left:414px}
.col-res{left:712px}
.col-other{left:928px}
.copyright{position:absolute;top:4868px;left:0;width:1200px;height:38px;background:var(--brown);color:var(--white);font-size:13px;display:flex;align-items:center;justify-content:center}
</style>
</head>
<body>

<header class="site-header">
  <div class="brand"><span class="brand-mark"></span><span class="brand-name">KEYSTONE<small>FLOORING FLORIDA</small></span></div>
  <nav class="nav"><span class="active">HOME</span><span>ABOUT US</span><span>OUR SERVICES</span><span>REVIEWS</span><span>BLOG</span><span>CONTACT US</span></nav>
  <span class="btn">Request Quote <i></i></span>
</header>

<div class="hero photo" role="img" aria-label="Bright white kitchen with island and warm hardwood flooring"></div>

<section class="intro">
  <h1>Experience premium flooring installationin Central Florida with Keystone Group</h1>
  <p>Are you tired of having your residential or commercial floors messed up by unprofessional services?<br>Allow Keystone Group to change your floor installation and removal story today with our premium services, creativity,<br>and personalized approach</p>
  <div class="actions"><span class="btn">Explore <i></i></span><span class="btn accent">Get your free estimate <i></i></span></div>
</section>

<section class="features">
  <div class="feature">
    <div class="icon-ring"><svg width="40" height="40" viewBox="0 0 40 40" fill="none" stroke="#333" stroke-width="1.6"><rect x="6" y="6" width="28" height="28"/><path d="M6 16h28M16 6v28M24 20l6 6"/></svg></div>
    <h3>MINIMAL STRESS ON<br>YOUR PLATE</h3>
    <p>Floor installation or removal can be stressful for both parties. You haverelocate most of your property on the affected area to a new location</p>
    <span class="link">VIEW MORE</span>
  </div>
  <div class="feature">
    <div class="icon-ring"><svg width="40" height="40" viewBox="0 0 40 40" fill="none" stroke="#333" stroke-width="1.6"><rect x="5" y="5" width="30" height="30"/><rect x="13" y="13" width="14" height="14"/><circle cx="20" cy="20" r="3"/></svg></div>
    <h3>A FLOOR WORTHY<br>OF YOUR HOME</h3>
    <p>The quality and type of your floor are as important as its style and appeal. The wrong combination could see you spending a lot on maintenance and feeling frustrate</p>
    <span class="link">VIEW MORE</span>
  </div>
  <div class="feature">
    <div class="icon-ring"><svg width="40" height="40" viewBox="0 0 40 40" fill="none" stroke="#333" stroke-width="1.6"><rect x="8" y="6" width="24" height="22"/><path d="M8 28l-3 7h30l-3-7M14 13h12M14 19h8"/></svg></div>
    <h3>QUALIFIED &amp; CERTIFIED<br>EXPERTS</h3>
    <p>After spending a lot to finally get that property of your dream, the last thing you want is some rookie messing it up and getting you back on your plans. Here at Keystone</p>
    <span class="link">VIEW MORE</span>
  </div>
</section>

<section class="partner">
  <div class="photo" role="img" aria-label="Open living room with sofas and dark hardwood floor"></div>
  <div class="copy">
    <h2>A RELIABLE PARTNER<br>TO LEAN ON</h2>
    <p>Keystone Group comes with over 14 years of experience in floor installation. We are specialists when it comes to tile installation, hardwood installation, carpet installation, tile backsplash installation, vinyl installation, laminate floor installation, and floor removal. Over the years, we have come to position ourselves as the professional hands our customers need for all their installation and removal needs. With us, you can be assured of on-time</p>
    <span class="btn">Learn more <i></i></span>
  </div>
</section>

<section class="services">
  <h2 class="section-title">Make your floors scream<br>quality &amp; beauty</h2>
  <div class="service-grid">
    <article class="service-card"><h3>TILE INSTALLATION</h3><div class="photo" role="img" aria-label="Worker laying large grey tiles on adhesive" style="background:linear-gradient(135deg,#4a4a4a,#8a8a88 60%,#d8d8d6)"></div><p>Tile is one durable flooring material that, when placed well, leaves your home or property looking luxurious &amp; inviting</p><span class="link">LEARN MORE</span></article>
    <article class="service-card"><h3>HARDWOOD INSTALLATION</h3><div class="photo" role="img" aria-label="Installer fitting hardwood planks with tape measure" style="background:linear-gradient(160deg,#7d93b0,#c9b8a6 45%,#e9e2da)"></div><p>Are you looking for the best hardwood installers near you? You are at the right place. Keystone Group is an expert</p><span class="link">LEARN MORE</span></article>
    <article class="service-card"><h3>LAMINATE INSTALLATION</h3><div class="photo" role="img" aria-label="Hands placing a laminate floor plank" style="background:linear-gradient(150deg,#f3e4d4,#d9a77a 50%,#a8693c)"></div><p>Adorning your floor with laminate material is often a great option to limit scratches, wear and tear, and improve floor</p><span class="link">LEARN MORE</span></article>
    <article class="service-card"><h3>CARPET INSTALLATION</h3><div class="photo" role="img" aria-label="Worker measuring and cutting carpet" style="background:linear-gradient(160deg,#3f6fb8,#b7a596 45%,#e6e1dc)"></div><p>Tile is one durable flooring material that, when placed well, leaves your home or property looking luxurious &amp; inviting</p><span class="link">LEARN MORE</span></article>
    <article class="service-card"><h3>VINYL INSTALLATION</h3><div class="photo" role="img" aria-label="Two workers installing vinyl panels" style="background:linear-gradient(135deg,#e8ece9,#8f9b96 50%,#4d5a55)"></div><p>Vinyl flooring is a great option for families and businesses looking for a balance between the deep texture and feel of real</p><span class="link">LEARN MORE</span></article>
    <article class="service-card"><h3>FLOOR REMOVAL</h3><div class="photo" role="img" aria-label="Workers pulling up old carpet" style="background:linear-gradient(170deg,#6f6a66,#b48a5d 50%,#d8c6a8)"></div><p>Removing your floor isn't an easy task, whether it is a carpet installation, hardwood, or concrete. It takes a lot of time</p><span class="link">LEARN MORE</span></article>
  </div>
</section>

<section class="testimonials">
  <div class="slider-arrows">
    <span><svg width="12" height="14" viewBox="0 0 12 14"><path d="M9 1L3 7l6 6" fill="none" stroke="#333" stroke-width="2"/></svg></span>
    <span><svg width="12" height="14" viewBox="0 0 12 14"><path d="M3 1l6 6-6 6" fill="none" stroke="#333" stroke-width="2"/></svg></span>
  </div>
  <h2>WHAT OUR CLIENTS SAYS</h2>
  <div class="avatar" role="img" aria-label="Client portrait"></div>
  <div class="divider"></div>
  <svg class="quote-mark" width="32" height="26" viewBox="0 0 32 26"><path d="M0 26V14C0 6 4 1 12 0v5c-4 1-6 4-6 8h6v13zM18 26V14c0-8 4-13 12-14v5c-4 1-6 4-6 8h6v13z" fill="#fff"/></svg>
  <blockquote>Lorem ipsum dolor sit amet, consectetur adipiscing elit, sed do eiusmod tempor incididunt ut labore et dolore magna aliqua. Ut enim ad minim veniam, quis nostrud exercitation ullamco laboris nisi ut aliquip ex ea commodo consequat.</blockquote>
  <span class="btn">View more <i></i></span>
  <cite>DANIEL MARSH</cite>
</section>

<section class="process">
  <h2 class="section-title">A simple, repeatable process</h2>
  <div class="steps">
    <div class="step">
      <svg width="44" height="44" viewBox="0 0 44 44" fill="none" stroke="#a86e36" stroke-width="1.8"><rect x="4" y="8" width="36" height="32"/><path d="M4 16h36M12 4v8M32 4v8"/><path d="M11 23h4M20 23h4M29 23h4M11 31h4M20 31h4M29 31h4" stroke="#333"/></svg>
      <h4>SCHEDULE AN<br>APPOINTMENT</h4>
      <p>Fill out the form on our site or call us on our hotline to relay your needs and schedule a free</p>
      <span class="link">VIEW MORE</span>
    </div>
    <div class="step">
      <svg width="44" height="44" viewBox="0 0 44 44" fill="none" stroke="#a86e36" stroke-width="1.8"><path d="M6 40V14L38 4v36z"/><path d="M6 27l32-10M22 9v31" stroke="#333"/></svg>
      <h4>YOUR PREFERRED<br>FLOOR MATERIAL</h4>
      <p>Based on our findings on consultation and our inspection, we will help you figure</p>
      <span class="link">VIEW MORE</span>
    </div>
    <div class="step">
      <svg width="44" height="44" viewBox="0 0 44 44" fill="none" stroke="#a86e36" stroke-width="1.8"><circle cx="22" cy="16" r="11"/><circle cx="22" cy="16" r="5" stroke="#333"/><path d="M15 26l-4 14 11-5 11 5-4-14"/></svg>
      <h4>PREMIUM<br>INSTALLATION</h4>
      <p>After the two stages are done, and you have approved the work date, our professionals for your floor</p>
      <span class="link">VIEW MORE</span>
    </div>
    <div class="step">
      <svg width="44" height="44" viewBox="0 0 44 44" fill="none" stroke="#a86e36" stroke-width="1.8"><circle cx="26" cy="13" r="9"/><path d="M26 8v10M23 11h5" stroke="#333"/><path d="M4 32h8l8 4h10l10-8M12 28h10"/></svg>
      <h4>A HAPPY<br>YOU</h4>
      <p>With a quality job done, go ahead and enjoy your floors for years to come with minimal maintenance</p>
      <span class="link">VIEW MORE</span>
    </div>
  </div>
</section>

<section class="get-started">
  <h2 class="section-title">Get started now</h2>
  <div class="form-row row-one"><label>APPOINTMENT</label><span class="field">Type of appointment</span><span class="field">Closest city</span><span class="field">Date</span></div>
  <div class="form-row row-two"><label>YOUR INFO</label><span class="field">Name</span><span class="field">Contact info</span><span class="field">Address</span></div>
</section>

<footer class="site-footer">
  <div class="brand"><span class="brand-mark"></span><span class="brand-name">KEYSTONE<small>FLOORING FLORIDA</small></span></div>
  <p class="footer-about">At vero eos et accusamus et iusto odio dignissimos ducimus qblanditiis praesentium voluptatum deleniti atque corrupti quos dolor</p>
  <div class="footer-col col-contact contact">
    <h4>FIND US ON</h4>
    <ul>
      <li><span class="ic"><svg width="10" height="14" viewBox="0 0 10 14"><path d="M5 0a5 5 0 0 0-5 5c0 4 5 9 5 9s5-5 5-9a5 5 0 0 0-5-5zm0 7a2 2 0 1 1 0-4 2 2 0 0 1 0 4z" fill="#a86e36"/></svg></span>520 Lorem Ipsum Dolor</li>
      <li><span class="ic"></span>Oakridge</li>
      <li><span class="ic"><svg width="12" height="12" viewBox="0 0 12 12"><path d="M2 0l2.5 3-1.5 1.5c.8 1.7 2.2 3.1 3.5 3.5L8 6.5 12 9l-1 3C5 12 0 7 0 1z" fill="#a86e36"/></svg></span>1 800 555 0142</li>
      <li><span class="ic"><svg width="13" height="10" viewBox="0 0 13 10" fill="none" stroke="#a86e36" stroke-width="1.3"><rect x=".6" y=".6" width="11.8" height="8.8"/><path d="M.6.6l5.9 5 5.9-5"/></svg></span>info@keystoneflooringfl.com</li>
    </ul>
  </div>
  <div class="footer-col col-res">
    <h4>RESOURCES</h4>
    <ul><li>Home</li><li>About Us</li><li>Services</li><li>Process</li><li>Contact &nbsp;Us</li></ul>
  </div>
  <div class="footer-col col-other">
    <h4>OTHER LINKS</h4>
    <ul><li>FAQ</li><li>Privacy Policy</li><li>Press &amp; Media</li><li>Help Service</li><li>Terms &amp; Conditions</li></ul>
  </div>
</footer>
<div class="copyright">© 2020 Keystone Flooring Florida. All Rights Reserved</div>

</body>
</html>
```